Business Card Design Project for Harbourlight Homes

We need a business card design for Harbourlight Homes Ltd, a respected building company that specialises in high quality designer homes.

We're after a sleek, clean, modern business card (could even have an interesting shape or something different from normal business cards) with wow factor that people will remember. It also needs to look sharp and great on print.

Please see example attached (do not copy, for inspiration only).

It needs to be in line with the new logo (see attached) and look consistent with that.

The new business card should include the Trusted Trades logo (see attached) as well as the company logo and the two need to look balanced and sleek in regards to their position on the card.
_______________________________________________________
Details to be included:
Tobin Vareck
Director

M: 021 555 0148
E: milo@harbourlighthomes.example
W: www.harbourlighthomes.example

If you present an option for an open card, here's some additional wording we would like you to use:

Harbourlight Homes are a highly skilled team who specialises in residential projects, from simple homes through to top end architectural designs.
We will treat your project with integrity, the attention it deserves, and we guarantee 100% satisfaction.

Timeless craftsmanship. Uncompromising standards.

___________________________________________________________
Additional info on Harbourlight Homes for your consideration:

The core values of the company are integrity, trust, expertise and uncompromising standards.

Harbourlight Homes have been building homes for over 20 years. Only residential, from simple 2-3 bedroom homes through to top end architectural designs. They are a registered Trusted Trade (the Trusted Trades Federation is a highly trusted and respected organisation in New Zealand).

The team at Harbourlight Homes pride themselves in delivering impeccable service to their clients and position themselves as their trusted partners and friends in the construction of their most valuable asset.

Thanks! We look forward to your designs!!!

Target Market(s)

People 30 yrs+ who have an interest in owning quality homes and are prepared to pay for it. Homes built to standards, future-proofed, building savvy.

Industry/Entity Type

Construction

Requirements
Must have
• We're looking for some wow factor as well and something that stands out and people will remember

The final design should communicate timeless craftsmanship, trust, special, VALUE, exquisite, stylish, standing the test of time, no cutting corners, reliability and high standards.

The final design also needs to be sharp and look great on print. The file supplied needs to be high resolution.

```html
<!DOCTYPE html>
<html lang="en">
<head>
<meta charset="utf-8">
<title>Harbourlight Homes Ltd – Business Card</title>
<link href="https://fonts.googleapis.com/css2?family=Barlow+Semi+Condensed:wght@400;500;600&display=swap" rel="stylesheet">
<style>
  :root {
    --backdrop: #2b2b2b;
    --card-white: #ffffff;
    --card-black: #141414;
    --card-black-top: #1c1c1c;
    --ink: #161616;
    --ink-soft: #2a2a2a;
    --accent-red: #e0262a;
    --rule-grey: #8a8a8a;
    --on-dark: #f2f2f2;
    --badge-neutral: #c9c9c9;
  }
  * { box-sizing: border-box; margin: 0; padding: 0; }
  html, body {
    width: 1200px; height: 900px; overflow: hidden;
    background: var(--backdrop);
    font-family: "Barlow Semi Condensed", "Arial Narrow", sans-serif;
  }
  .stage {
    position: relative; width: 1200px; height: 900px;
    display: flex; justify-content: center; align-items: center; gap: 70px;
  }
  .card {
    position: relative; width: 330px; height: 540px;
    clip-path: polygon(34px 0, 296px 0, 330px 34px, 330px 506px, 296px 540px, 34px 540px, 0 506px, 0 34px);
  }
  .card--front { background: var(--card-white); color: var(--ink); }
  .card--back {
    background: linear-gradient(180deg, var(--card-black-top) 0%, var(--card-black) 60%);
    color: var(--on-dark);
  }
  .wordmark {
    position: absolute; left: 40px; right: 40px;
    display: flex; align-items: center; gap: 12px;
  }
  .wordmark__square { width: 40px; height: 40px; background: var(--accent-red); flex: none; }
  .wordmark__name {
    font-weight: 600; font-size: 24px; line-height: 1.02; letter-spacing: 1.5px;
    text-transform: uppercase;
  }
  .card--front .wordmark { top: 70px; }
  .card--back .wordmark { top: 318px; }
  .wordmark-rule {
    position: absolute; left: 40px; right: 40px; height: 1px; background: var(--rule-grey);
  }
  .card--front .wordmark-rule { top: 124px; }
  .card--back .wordmark-rule { top: 372px; }
  .accent-rule {
    position: absolute; left: 40px; width: 120px; height: 3px; background: var(--accent-red);
  }
  .card--front .accent-rule { top: 132px; }
  .card--back .accent-rule { top: 380px; }

  .contact {
    position: absolute; top: 180px; left: 0; right: 0; text-align: center;
    text-transform: uppercase; color: var(--ink);
  }
  .contact__name { font-size: 19px; font-weight: 500; letter-spacing: 1px; }
  .contact__role { font-size: 12px; letter-spacing: 1px; margin-top: 1px; }
  .contact__details { margin-top: 22px; font-size: 14px; line-height: 1.3; letter-spacing: 0.6px; }

  .about {
    position: absolute; top: 370px; left: 36px; right: 36px;
    font-size: 11.5px; line-height: 1.25; letter-spacing: 0.4px;
    text-transform: uppercase; color: var(--ink-soft);
  }
  .about p + p { margin-top: 8px; }

  .member-badge {
    position: absolute; bottom: 48px; left: 50%; transform: translateX(-50%);
    width: 30px; height: 30px;
    background: var(--badge-neutral);
  }

  .web-address {
    position: absolute; top: 416px; left: 0; right: 0; text-align: center;
    font-size: 14px; letter-spacing: 1px; text-transform: uppercase;
  }
</style>
</head>
<body>
<main class="stage">
  <section class="card card--front" aria-label="Card front">
    <div class="wordmark">
      <span class="wordmark__square"></span>
      <span class="wordmark__name">Harbourlight<br>Homes Ltd</span>
    </div>
    <div class="wordmark-rule"></div>
    <div class="accent-rule"></div>

    <div class="contact">
      <p class="contact__name">Tobin Vareck</p>
      <p class="contact__role">Director</p>
      <div class="contact__details">
        <p>021 555 0148</p>
        <p>milo@harbourlighthomes.example</p>
        <p>www.harbourlighthomes.example</p>
      </div>
    </div>

    <div class="about">
      <p>Our highly skilled team specialise in residential projects, from simple homes through to top end architectural designs.</p>
      <p>We will treat your project with integrity and we guarantee 100% satisfaction.</p>
    </div>

    <div class="member-badge" role="img" aria-label="Trusted Trades member badge"></div>
  </section>

  <section class="card card--back" aria-label="Card back">
    <div class="wordmark">
      <span class="wordmark__square"></span>
      <span class="wordmark__name">Harbourlight<br>Homes Ltd</span>
    </div>
    <div class="wordmark-rule"></div>
    <div class="accent-rule"></div>
    <p class="web-address">www.harbourlighthomes.example</p>
  </section>
</main>
</body>
</html>
```